Tollbury Malt Keller Beer Bottle Label #1

A beer bottle label is required for TMK's first beer that will go on sale later this year.
It is hoped that an on-going relationship will be formed with the successful designer.
Designs for glasses, packaging, t-shirts etc will also be required later this year.
Designs should reflect the local origin of the brewery and project an image of tradition and quality.
Designs should be simple, clean, classic and classy.
Designs should not be loud, bright, crazy or busy.
Design should include an element that can be used as brewery logo.
'Malt Keller' to be prominent, 'Tollbury' to be discreet.
Name of first beer to be Tollmo-Dunkel - label shall be easily adapted for different beers e.g. Tollmo-Weiss.
Deliverables include a smaller text only label for back of the bottle.

***I also need a logo that goes with my label design. So whoever submitted a logo that I like will be selected as the 2nd place winner.

Please refer to the attachment on this brief.

Requirements
Must have
• See uploaded design brief.
Nice to have
Should not have

```html
<!DOCTYPE html>
<html lang="en">
<head>
<meta charset="utf-8">
<title>Tollbury Malt Keller – Tollmo Dunkel Label</title>
<link rel="stylesheet" href="https://fonts.googleapis.com/css2?family=Alfa+Slab+One&family=Libre+Baskerville:wght@700&family=Rye&display=swap">
<style>
  :root {
    --ink: #0d0d0d;
    --label-red: #a72228;
    --paper: #ffffff;
    --mist: #e6e6e6;
    --art-tone: #d4d4d4;
  }
  html, body {
    margin: 0;
    padding: 0;
    width: 1200px;
    height: 1200px;
    overflow: hidden;
    background: var(--paper);
  }
  .label {
    display: block;
    width: 1200px;
    height: 1200px;
  }
  .frame-outer { fill: var(--ink); }
  .frame-red { fill: var(--label-red); }
  .frame-paper { fill: var(--paper); }
  .frame-dots { fill: none; stroke: var(--ink); stroke-width: 4; stroke-dasharray: 3 4; }
  .field-mist { fill: var(--mist); }
  .field-red { fill: var(--label-red); }
  .field-edge { fill: none; stroke: var(--ink); stroke-width: 1.5; stroke-dasharray: 10 4 2 4; opacity: .6; }
  .horizon { stroke: var(--ink); stroke-width: 4; }
  .stag-art { fill: var(--art-tone); }
  .since-band { fill: var(--ink); }
  .since-text {
    font-family: "Libre Baskerville", Georgia, serif;
    font-weight: 700;
    font-size: 50px;
    fill: var(--paper);
  }
  .spec-text {
    font-family: "Libre Baskerville", Georgia, serif;
    font-weight: 700;
    font-size: 46px;
    fill: var(--ink);
  }
  .brand-mark {
    font-family: "Alfa Slab One", Georgia, serif;
    font-size: 300px;
    fill: var(--paper);
  }
  .brand-line {
    font-family: "Alfa Slab One", Georgia, serif;
    font-size: 50px;
    fill: var(--paper);
  }
  .ribbon-edge { fill: var(--ink); }
  .ribbon-face { fill: var(--mist); }
  .ribbon-rule { fill: none; stroke: var(--ink); stroke-width: 3; }
  .beer-name {
    font-family: "Rye", Georgia, serif;
    font-size: 96px;
    fill: var(--ink);
  }
</style>
</head>
<body>
<svg class="label" viewBox="0 0 1500 1500" xmlns="http://www.w3.org/2000/svg" aria-label="Tollbury Malt Keller Tollmo Dunkel bottle label">
  <defs>
    <clipPath id="inner-field">
      <polygon points="750,100 1400,750 750,1400 100,750"/>
    </clipPath>
  </defs>

  <!-- diamond frame -->
  <g class="diamond-frame">
    <polygon class="frame-outer" points="750,0 1500,750 750,1500 0,750"/>
    <polygon class="frame-red" points="750,22 1478,750 750,1478 22,750"/>
    <polygon class="frame-outer" points="750,50 1450,750 750,1450 50,750"/>
    <polygon class="frame-paper" points="750,60 1440,750 750,1440 60,750"/>
    <polygon class="frame-dots" points="750,72 1428,750 750,1428 72,750"/>
  </g>

  <!-- inner field -->
  <g class="inner-field" clip-path="url(#inner-field)">
    <rect class="field-mist" x="0" y="0" width="1500" height="1500"/>
    <rect class="field-red" x="0" y="648" width="1500" height="520"/>
    <polygon class="field-edge" points="750,120 1380,750 750,1380 120,750"/>
    <line class="horizon" x1="0" y1="648" x2="1500" y2="648"/>
  </g>

  <!-- stag illustration area -->
  <rect class="stag-art" x="470" y="262" width="560" height="384" rx="40"
        role="img" aria-label="Hand-drawn illustration of a resting stag with large antlers"/>

  <!-- since banner -->
  <g class="since-banner">
    <polygon class="frame-red" points="455,170 1045,160 1030,250 470,255"/>
    <polygon class="since-band" points="478,182 1020,168 1000,232 498,240"/>
    <text class="since-text" x="750" y="222" text-anchor="middle" textLength="270" lengthAdjust="spacingAndGlyphs">SINCE 1997</text>
  </g>

  <!-- brand block -->
  <text class="spec-text" x="383" y="828" text-anchor="middle" textLength="170" lengthAdjust="spacingAndGlyphs">500 ML</text>
  <text class="spec-text" x="1107" y="836" text-anchor="middle" textLength="225" lengthAdjust="spacingAndGlyphs">ABV 4.6%</text>

  <text class="brand-mark" x="742" y="928" text-anchor="middle" textLength="462" lengthAdjust="spacingAndGlyphs">TMK</text>
  <text class="brand-line" x="735" y="990" text-anchor="middle" textLength="440" lengthAdjust="spacing">MALT KELLER</text>
  <text class="brand-line" x="735" y="1046" text-anchor="middle" textLength="448" lengthAdjust="spacing">TOLLBURY</text>

  <!-- name ribbon -->
  <g class="name-ribbon">
    <path class="frame-red" d="M285,1050 L1195,1050 L1200,1330 L290,1335 Z"/>
    <path class="ribbon-edge" d="M300,1092 Q720,1045 1172,1078 L1196,1302 Q720,1268 312,1330 Z"/>
    <path class="ribbon-face" d="M318,1106 Q720,1062 1158,1092 L1178,1288 Q720,1256 328,1314 Z"/>
    <path class="ribbon-rule" d="M330,1120 Q720,1078 1146,1106 L1164,1276 Q720,1244 340,1300 Z"/>
    <text class="beer-name" x="748" y="1238" text-anchor="middle" textLength="660" lengthAdjust="spacingAndGlyphs" transform="rotate(-2 748 1210)">TOLLMO DUNKEL</text>
  </g>
</svg>
</body>
</html>
```